Advertisements for web banners and street signage

Role Finch is a New Zealand Job Board (career vacancy search) website that requires some creative ad banners for promotion online, at events, and on street signage.

Our role finch logo is attached in low resolution, and in high resolution, the logo, slogan, and website should be incorporated somewhere in the ad. Ads should be long in length (not square) either vertical or horizontal.

I've attached some examples of ads

Target Market(s)

Working population. We exist to bring more choice to New Zealand job seekers and save job seekers time. We are about "finding your next job"

Industry/Entity Type

Recruitment

Requirements
Must have
• Use of bright colours. Gets your attention.
Nice to have
• A funny image or joke related to finding a job that catches your attention e.g. could play on the use of Role Finch = job "sauce"
• A slogan, pun, or sentence related to finding a job that catches your attention, An example of a slogans "some say a change is as good as a holiday"
Should not have
• Swearing or sexism

```html
<!DOCTYPE html>
<html lang="en">
<head>
<meta charset="utf-8">
<title>Role Finch – Web Banner</title>
<link rel="stylesheet" href="https://fonts.googleapis.com/css2?family=Ubuntu:wght@400;500;700&display=swap">
<style>
  :root {
    --teal: #00b3a4;
    --ink: #111111;
    --grey-dark: #555555;
    --grey-tag: #8a8a8a;
    --page: #f2f2f2;
    --white: #ffffff;
  }
  html, body {
    margin: 0;
    width: 1200px;
    height: 1200px;
    overflow: hidden;
    background: var(--page);
  }
  .stage {
    width: 1200px;
    height: 1200px;
    display: flex;
    align-items: center;
    justify-content: center;
  }
  .banner {
    display: block;
    width: 1120px;
    height: 480px;
    font-family: "Ubuntu", sans-serif;
  }
  .brand-name { fill: var(--teal); font-weight: 500; font-size: 36px; }
  .brand-tagline { fill: var(--grey-tag); font-size: 10px; letter-spacing: 3px; }
  .headline { font-weight: 500; }
  .headline .accent { fill: var(--teal); }
  .headline .dark { fill: var(--ink); }
  .cta-label { fill: var(--white); font-weight: 500; font-size: 46px; }
</style>
</head>
<body>
<main class="stage">
  <svg class="banner" viewBox="0 0 1183 507" xmlns="http://www.w3.org/2000/svg">
    <defs>
      <linearGradient id="asphalt" x1="0" y1="0" x2="1" y2="1">
        <stop offset="0" stop-color="#9a9a9a"/>
        <stop offset="1" stop-color="#7c7c7c"/>
      </linearGradient>
      <linearGradient id="clockface" x1="0" y1="0" x2="1" y2="1">
        <stop offset="0" stop-color="#d9c9a6"/>
        <stop offset="1" stop-color="#efe4cc"/>
      </linearGradient>
      <linearGradient id="button" x1="0" y1="0" x2="0" y2="1">
        <stop offset="0" stop-color="#6a6a6a"/>
        <stop offset="1" stop-color="#262626"/>
      </linearGradient>
    </defs>

    <rect class="banner-bg" width="1183" height="507" fill="var(--white)"/>

    <!-- accent bands -->
    <polygon class="band-teal" points="786,0 806,0 630,472 1072,472 1060,507 598,507" fill="var(--teal)"/>
    <polygon class="band-grey" points="1072,472 1183,472 1183,507 1060,507" fill="var(--grey-dark)"/>
    <polygon class="divider-teal" points="527,0 539,0 353,507 341,507" fill="var(--teal)"/>
    <polygon class="divider-teal" points="0,178 441,234 441,242 0,186" fill="var(--teal)"/>

    <!-- photo panels -->
    <g role="img" aria-label="Photo: feet standing on asphalt before yellow painted arrows pointing left, ahead and right">
      <polygon points="0,187 438,242 336,507 0,507" fill="url(#asphalt)"/>
    </g>
    <g role="img" aria-label="Photo: feet on asphalt below a painted arrow and the word change">
      <polygon points="543,7 786,7 693,257 452,257" fill="url(#asphalt)"/>
    </g>
    <g role="img" aria-label="Photo: clock face reading time for change">
      <polygon points="448,267 689,267 601,507 361,507" fill="url(#clockface)"/>
    </g>

    <!-- brand -->
    <g class="brand">
      <text class="brand-name" x="60" y="101" textLength="300" lengthAdjust="spacingAndGlyphs">ROLE FINCH</text>
      <text class="brand-tagline" x="61" y="118" textLength="298" lengthAdjust="spacing">FINDING YOUR NEXT JOB IN NZ</text>
    </g>

    <!-- headline -->
    <g class="headline">
      <text class="accent" x="811" y="124" font-size="58" textLength="305" lengthAdjust="spacingAndGlyphs">SOME SAY</text>
      <text class="dark" x="811" y="186" font-size="58" textLength="304" lengthAdjust="spacingAndGlyphs">A CHANGE</text>
      <text class="accent" x="811" y="245" font-size="58" textLength="310" lengthAdjust="spacingAndGlyphs">IS AS GOOD</text>
      <text class="dark" x="811" y="292" font-size="44" textLength="311" lengthAdjust="spacingAndGlyphs">AS A HOLIDAY</text>
    </g>

    <!-- call to action -->
    <g class="cta">
      <rect x="799" y="339" width="322" height="71" rx="35.5" fill="url(#button)"/>
      <text class="cta-label" x="846" y="392" textLength="192" lengthAdjust="spacingAndGlyphs">VISIT US</text>
      <circle cx="1081" cy="375" r="22" fill="var(--white)"/>
      <polygon points="1069,375 1088,364 1088,386" fill="var(--teal)"/>
    </g>
  </svg>
</main>
</body>
</html>
```